Popular Golf Club needs attractive brochure

We need a brochure that will attract golfers to come to the Kestrel River area and the Brindlebay Golf Club for their golfing holiday. It also needs to address the availability of a function area and corporate functions in the clubhouse and corporate golf days on the course as well.
It will highlight our direct phone contact numbers and website as well.
We are a 36 Hole Championship Golf Course on the Kestrel River border of NSW and Victoria. 3 hours easy freeway drive from Melbourne. Over 300 sunny days every year. Fabulous golf weather all year round. Raincheck guarantee (if it rains we will give you free golf on you next visit).
The area is a golf and watersport playground. Sandy beaches, the mighty Kestrl River, home of the giant Kestrel Perch, fishing, camping, boating and golf all on your doorstep.
We can arrange Golf packages for individuals and groups including 3 and 4 star accommodation available all year round.

Target Market(s)

Golfers looking for holidays

Industry/Entity Type

Accommodation

Requirements
Must have
• Branding bar and logo. Colours signifying sun, grass and river.
Nice to have
• Smiling happy golfers, particularly more senior age group. Map of location and proximity to Melbourne. Photos of the course. some attached, many more available.

```html
<!DOCTYPE html>
<html lang="en">
<head>
<meta charset="utf-8">
<title>Brindlebay Golf Club – Inner Spread</title>
<link href="https://fonts.googleapis.com/css2?family=Open+Sans:wght@400;600;700&family=Lato:wght@300;400&display=swap" rel="stylesheet">
<style>
  :root{
    --page:#f1ede6;
    --paper:#ffffff;
    --grass:#8dc63f;
    --river:#4db6c8;
    --sun:#f5c400;
    --ink:#1e1e1e;
    --rule:#3a3a3a;
  }
  *{margin:0;padding:0;box-sizing:border-box}
  html,body{width:1200px;height:978px;overflow:hidden;background:var(--page)}
  .brochure{
    position:absolute;left:40px;top:91px;width:805px;height:572px;
    background:var(--paper);transform:scale(1.3913);transform-origin:0 0;
    font-family:"Open Sans",Arial,sans-serif;color:var(--ink);overflow:hidden;
    box-shadow:0 2px 8px rgba(0,0,0,.15);
  }
  .panel-rule{position:absolute;top:0;width:1px;height:478px;background:var(--rule)}
  .photo{position:absolute}
  .photo-caption{position:absolute;color:#fff;font-size:13px;letter-spacing:.3px;text-shadow:0 0 3px rgba(0,0,0,.6)}
  .photo-subcaption{position:absolute;color:#fff;font-size:7px;text-shadow:0 0 2px rgba(0,0,0,.6);white-space:nowrap}
  .section-tag{position:absolute;height:16px;display:flex;align-items:center;gap:5px}
  .section-tag .pill{background:var(--grass);color:#fff;font-weight:700;font-size:10.5px;padding:0 10px;height:16px;line-height:16px;border-radius:8px 0 0 8px}
  .section-tag .dot{width:10px;height:10px;border-radius:50%;background:var(--sun)}
  .body-copy{position:absolute;font-size:9.6px;line-height:13.4px}
  .body-copy p{margin:0}
  .brand-band{position:absolute;left:0;top:486px;width:805px;height:86px;background:var(--grass)}
  .brand-stripe{position:absolute;left:0;width:805px}
  .brand-stripe.river{top:472px;height:5px;background:var(--river)}
  .brand-stripe.sun{top:479px;height:5px;background:var(--sun)}
  .tagline{position:absolute;left:0;width:805px;top:516px;text-align:center;color:#fff;font-family:"Lato",Arial,sans-serif;font-weight:300;font-size:26px;letter-spacing:.6px}
</style>
</head>
<body>
<div class="brochure">

  <div class="photo" style="left:0;top:0;width:268px;height:95px;background:linear-gradient(#e9eef2 0%,#cfd6d9 45%,#6e6a55 60%,#4f7a34 100%)" role="img" aria-label="Clubhouse exterior at dusk with car park"></div>
  <div class="photo" style="left:17px;top:111px;width:99px;height:73px;background:linear-gradient(#8fa86a,#6b7f4c)" role="img" aria-label="Members relaxing at outdoor tables"></div>
  <div class="photo" style="left:141px;top:111px;width:100px;height:73px;background:linear-gradient(#8a4a2c,#3a2720)" role="img" aria-label="Function room filled with guests"></div>

  <div class="section-tag" style="left:17px;top:199px">
    <span class="pill">Club house</span><span class="dot"></span>
  </div>

  <div class="body-copy" style="left:17px;top:224px;width:245px">
    <p>Our modern Club house boasts full NSW club facilities and invites members and visitors to choose seating are as overlooking the course or dine Al Fresco on the balcony amongst the nature. Our Bistro is open all day every day for full bistro meals as well as light snacks.</p>
    <p>The Pro Shop has all your golfing requirements with a fleet of Yarrow golf carts and club and equipment hire and sales. The driving range is complimented by large chipping and putting greens and golf balls are available during daylight hours. Outstanding value golf packages offer a range of accommodation options within easy walking distance of the Clubhouse.</p>
    <p>Let our friendly staff make your stay an unforgettable golfing experience.</p>
  </div>

  <div class="photo" style="left:268px;top:0;width:267px;height:133px;background:linear-gradient(#cfe0ee 0%,#dfe6e2 18%,#5e8a45 40%,#7fae52 75%,#93c060 100%)" role="img" aria-label="Pro shop building with flags and gardens"></div>
  <div class="photo-caption" style="left:276px;top:100px">Brindlebay Golf Club Pro Shop</div>
  <div class="photo-subcaption" style="left:276px;top:117px">Stocklist of Fairline, Parvale, Greenhollow, Ironbark, Coveridge and more</div>

  <div class="section-tag" style="left:288px;top:154px">
    <span class="pill">Established</span><span class="dot"></span>
  </div>

  <div class="body-copy" style="left:288px;top:188px;width:245px">
    <p>The Club and course occupy the original site of the 1942-1960 Commonwealth Air Corps base once the largest air base in the Southern Hemisphere.</p>
    <p>During WWII it was the home of the famous Skylark Bomber, which is now commemorated with a scale model proudly displayed at the main entrance to the Golf Course. The village of Wattlecove is renowned for its friendly atmosphere and the many and varied activities available in the region.</p>
  </div>

  <div class="photo" style="left:291px;top:350px;width:104px;height:78px;background:linear-gradient(#b7cfd8 0%,#6f8f4c 45%,#4c6a34 100%)" role="img" aria-label="Golfers gathered under marquees"></div>
  <div class="photo" style="left:406px;top:350px;width:107px;height:78px;background:linear-gradient(#d8e3e6 0%,#7da35a 45%,#5b8c3c 100%)" role="img" aria-label="Tournament day on the green"></div>

  <div class="photo" style="left:537px;top:0;width:268px;height:130px;background:linear-gradient(#bcd3e6 0%,#c9d6c6 35%,#7e8a62 60%,#8b8a70 80%,#f4f4f2 100%)" role="img" aria-label="Riverbank with gum trees and historic bridge"></div>
  <div class="photo-caption" style="left:660px;top:88px;line-height:18px">“Nestled in Historic<br>&nbsp;&nbsp;&nbsp;Wattlecove...”</div>

  <div class="photo" style="left:561px;top:139px;width:103px;height:77px;background:linear-gradient(#8fa7a0,#a79e84)" role="img" aria-label="Sandy river beach with camping"></div>
  <div class="photo" style="left:688px;top:139px;width:104px;height:77px;background:linear-gradient(#b7d2e6 0%,#5c8a3d 45%,#d48fa4 75%,#5b8a3a 100%)" role="img" aria-label="Rose garden beside the course"></div>

  <div class="body-copy" style="left:553px;top:240px;width:245px">
    <p>The Kestrel River near Wattlecove has dozens of beautiful white sandy beaches with fantastic boating and camping areas. Fishermen regularly land record Kestrel Perch and our stretch of the river is a watersports playground.</p>
    <p>Just an easy 3-hour drive from Melbourne will bring you to ‘golfing heaven’ at Wattlecove</p>
  </div>

  <div class="photo" style="left:540px;top:355px;width:265px;height:112px;background:linear-gradient(90deg,#f4f4f2 0%,#c9cdc6 25%,#8f9a86 55%,#7a8a76 100%)" role="img" aria-label="Giant fish sculpture landmark"></div>
  <div class="photo-caption" style="left:543px;top:448px;font-size:11px">Wattlecove:</div>

  <div class="panel-rule" style="left:268px;height:470px"></div>
  <div class="panel-rule" style="left:535px;height:470px"></div>

  <div class="brand-stripe river"></div>
  <div class="brand-stripe sun"></div>
  <div class="brand-band"></div>
  <div class="tagline">"A great golf course is just the beginning..."</div>

</div>
</body>
</html>
```